Redesign existing website

We would like a redesign of the website http://www.velbrisanalytics.com that creates a more modern, up to date look.

Velbris Analytics creates software for social science research and is focused on making the software user friendly and easy to use. We would like to convey seriousness, but also
a very up to date, just released look.

Feel free to modify the logo if you wish.

Target Market(s)

Academics, researchers

Industry/Entity Type

Software

Requirements
Must have
• The design should incorporate the same information as the current website.

```html
<!DOCTYPE html>
<html lang="en">
<head>
<meta charset="utf-8">
<title>Velbris Analytics</title>
<link rel="stylesheet" href="https://fonts.googleapis.com/css2?family=Tinos:wght@400;700&family=Arimo:wght@400&family=Questrial&display=swap">
<style>
  :root {
    --bg: #b6d1ca;
    --bg-light: #cfe1dc;
    --brand-blue: #223f96;
    --ribbon: #2452c8;
    --ribbon-dark: #1a3a9c;
    --nav-active: #26408f;
    --tagline: #6a8882;
    --mission: #e0962f;
    --ink: #111;
    --grey-text: #555;
    --soft-grey: #8a8a8a;
    --panel: #ffffff;
    --box-left: #f1f1f1;
    --hero-top: #6d8191;
    --hero-mid: #4a5052;
    --hero-low: #4d6846;
  }
  * { margin: 0; padding: 0; box-sizing: border-box; }
  html, body { width: 1200px; height: 989px; overflow: hidden; }
  body {
    position: relative;
    background:
      radial-gradient(ellipse 700px 120px at 600px 300px, rgba(255,255,255,.35), transparent 70%),
      radial-gradient(ellipse 500px 100px at 150px 560px, rgba(255,255,255,.25), transparent 70%),
      linear-gradient(var(--bg), var(--bg-light) 35%, var(--bg) 70%);
    font-family: "Tinos", serif;
  }
  .brand { position: absolute; left: 118px; top: 16px; }
  .brand-mark { position: absolute; left: 56px; top: 0; width: 78px; height: 78px; border-radius: 50%; background: var(--brand-blue); border: 3px solid #fff; box-shadow: 0 0 0 1px #8aa; }
  .brand-name { position: absolute; left: 0; top: 86px; width: 210px; font-size: 24px; color: var(--brand-blue); white-space: nowrap; }
  .main-nav { position: absolute; top: 47px; left: 369px; }
  .main-nav a {
    position: absolute; font-weight: 700; font-size: 16px; color: #fff; text-decoration: none;
    text-shadow: 1px 1px 1px rgba(0,0,0,.35); white-space: nowrap;
  }
  .main-nav a.active { color: var(--nav-active); text-shadow: 1px 1px 0 rgba(255,255,255,.5); }
  .tagline {
    position: absolute; top: 228px; left: 118px; width: 978px; text-align: center;
    font-weight: 700; font-size: 21px; color: var(--tagline); letter-spacing: .4px;
    text-shadow: 0 1px 0 rgba(255,255,255,.5);
  }
  .panel {
    position: absolute; left: 112px; top: 294px; width: 980px; height: 595px;
    background: var(--panel); box-shadow: 0 0 4px rgba(0,0,0,.2);
  }
  .hero {
    position: absolute; left: 131px; top: 314px; width: 943px; height: 342px;
    border: 2px solid #ccc;
    background: linear-gradient(var(--hero-top), var(--hero-mid) 50%, var(--hero-low));
  }
  .ribbon { position: absolute; left: 196px; top: 274px; }
  .ribbon-text {
    position: absolute; left: 265px; top: 285px; width: 675px; text-align: center;
    color: #fff; font-size: 23px; text-shadow: 1px 1px 2px rgba(0,0,0,.6);
  }
  .info { position: absolute; left: 130px; top: 660px; width: 944px; height: 208px; border: 1px solid #ddd; background: #fafafa; }
  .mission { position: absolute; left: 0; top: 0; width: 632px; height: 100%; background: linear-gradient(var(--box-left) 60%, #e6ecea); }
  .mission h2 { position: absolute; left: 27px; top: 12px; font-size: 25px; color: var(--mission); font-weight: 700; }
  .mission p { position: absolute; left: 28px; width: 580px; font-family: "Arimo", sans-serif; font-size: 13.3px; line-height: 20px; color: var(--ink); }
  .mission .p1 { top: 52px; }
  .mission .p2 { top: 112px; }
  .product { position: absolute; left: 632px; top: 0; width: 312px; height: 100%; text-align: center; }
  .product h3 { font-weight: 400; font-size: 27px; color: var(--grey-text); margin-top: 13px; }
  .product .note { font-family: "Arimo", sans-serif; font-size: 14px; color: var(--soft-grey); margin-top: 2px; }
  .download {
    position: absolute; left: 23px; top: 82px; width: 277px; height: 70px; border-radius: 35px;
    background: linear-gradient(#fbfbfb, #d9d9d9 60%, #c4c4c4);
    box-shadow: 0 3px 5px rgba(0,0,0,.35), inset 0 1px 0 #fff; text-decoration: none;
  }
  .download svg { position: absolute; left: 10px; top: 10px; }
  .download .label { position: absolute; left: 66px; top: 11px; font-family: "Questrial", sans-serif; font-size: 27px; color: #555; text-align: left; white-space: nowrap; }
  .download .sub { position: absolute; left: 67px; top: 44px; font-size: 12px; color: #666; white-space: nowrap; }
  .login { position: absolute; right: 14px; bottom: 3px; font-size: 13px; color: #444; text-decoration: none; }
</style>
</head>
<body>
  <header>
    <div class="brand"><span class="brand-mark"></span><span class="brand-name">Velbris Analytics</span></div>
    <nav class="main-nav">
      <a class="active" style="left:0">HOME</a>
      <a style="left:73px">PRODUCTS</a>
      <a style="left:182px">NEWS</a>
      <a style="left:251px">ABOUT US</a>
      <a style="left:354px">CONTACT US</a>
    </nav>
  </header>

  <h1 class="tagline">INCREASING THE POWER AND EFFICIENCY OF EMPIRICAL SOCIAL SCIENCE RESEARCH</h1>

  <section class="panel"></section>
  <div class="hero" role="img" aria-label="Photograph of a mountain valley with snow patches above a calm lake and green meadow"></div>

  <svg class="ribbon" width="814" height="66" viewBox="0 0 814 66" aria-hidden="true">
    <polygon points="0,14 69,14 69,64 12,64 32,39" fill="var(--ribbon-dark)"/>
    <polygon points="814,14 745,14 745,64 802,64 782,39" fill="var(--ribbon-dark)"/>
    <polygon points="69,50 69,64 80,50" fill="#0f2570"/>
    <polygon points="745,50 745,64 734,50" fill="#0f2570"/>
    <rect x="69" y="0" width="676" height="50" fill="var(--ribbon)"/>
    <rect x="69" y="0" width="676" height="25" fill="#fff" opacity=".12"/>
  </svg>
  <div class="ribbon-text">Empowering the social science researcher</div>

  <section class="info">
    <div class="mission">
      <h2>Our mission</h2>
      <p class="p1">The mission of Velbris Analytics, Inc. is to produce software products that multiply the power and efficiency of empirical scientific research in the social sciences.</p>
      <p class="p2">A central goal is to expand access to complex data sources and to the advanced methods of scientific investigation needed to analyze them. habitasse platea dictumst. Pellentesque faucibus mauris sed nisl cursus ullamcorper. Proin placerat velit ac nisi scelerisque sit amet facilisis nunc suscipit. Duis quis lobortis tortor.</p>
    </div>
    <div class="product">
      <h3>Velbris Data Manager</h3>
      <div class="note">Preview Release Available!</div>
      <a class="download" href="#">
        <svg width="48" height="48" viewBox="0 0 48 48" aria-hidden="true">
          <circle cx="24" cy="24" r="22" fill="#4a4a4a" stroke="#999" stroke-width="2"/>
          <polyline points="16,15 24,23 32,15" fill="none" stroke="#ddd" stroke-width="4"/>
          <polyline points="16,25 24,33 32,25" fill="none" stroke="#ddd" stroke-width="4"/>
        </svg>
        <span class="label">Download Now</span>
        <span class="sub">Download Preview Release</span>
      </a>
      <a class="login" href="#">Log in</a>
    </div>
  </section>
</body>
</html>
```